I need to have a full website designed for a new consultancy business I'm trying to establish. It's called Brightpath consult. I need an English version to begin with, and then there should be a Danish version as well, but I'll translate that myself. Just be aware that I need two language versions. The consultancy field that I'm targeting is Leadership - and specialist development. I offer to facilitate corporate academies for global companies as well as specific workshops within leadership- or team development, strategy sessions, personal coaching and facilitation of D&I (Diversity and inclusion) workshops. BTW my logo is not in high resolution - I need that as well.

Target Market(s)

Larger companies that has a need for developing their inhouse leadership capabilities or that wants to develop their specialists to take on more responsibility.

Industry/Entity Type

Consultancy business

Coding

Number of Pages Required

Requirements
Must have
• Introduction site with a catch phrase. Book a meeting. Services that's beeing offered. Blog site with white papers etc. Language toggle (Danish/English). Cases/testimonials. About site. Contact site.

```html
<!DOCTYPE html>
<html lang="en">
<head>
<meta charset="utf-8">
<title>Brightpath Consult – Leadership &amp; Specialist Development</title>
<link href="https://fonts.googleapis.com/css2?family=Roboto:wght@300;400;500;700;900&display=swap" rel="stylesheet">
<style>
:root{
  --blue:#1f7ac4;
  --blue-deep:#1565b0;
  --blue-light:#2b8fd6;
  --ink:#111418;
  --text:#3a3f45;
  --muted:#6b7076;
  --grey-bg:#efefef;
  --footer-bg:#f3f4f6;
  --white:#ffffff;
}
*{box-sizing:border-box;margin:0;padding:0}
html,body{width:1200px;height:4081px;overflow:hidden}
body{font-family:'Roboto',sans-serif;color:var(--text);background:var(--white);position:relative}
.section{position:absolute;left:0;width:1200px}
.abs{position:absolute}
.eyebrow{font-size:18px;font-weight:500;color:var(--blue);letter-spacing:.3px}
.title{font-weight:700;color:var(--ink);text-transform:uppercase;white-space:nowrap}
.rule{width:50px;height:3px;background:var(--blue)}
.center{left:0;width:1200px;text-align:center}
.btn{display:flex;align-items:center;justify-content:center;color:#fff;background:var(--blue);font-size:17px;font-weight:500;letter-spacing:.3px;text-transform:uppercase;clip-path:polygon(6% 0,100% 0,94% 100%,0 100%)}

/* header */
.site-header{top:0;height:89px;background:#fff;z-index:5}
.brand{left:111px;top:28px;font-size:27px;font-weight:700;color:var(--ink);line-height:32px;white-space:nowrap}
.nav{top:34px;left:442px;font-size:15px;font-weight:500;color:var(--ink)}
.nav a{color:inherit;text-decoration:none;position:absolute;white-space:nowrap}
.nav .active{color:var(--blue)}
.nav .active::after{content:"";position:absolute;left:0;right:0;bottom:-9px;height:2px;background:var(--blue)}

/* hero */
.hero{top:89px;height:571px;background:linear-gradient(90deg,#f5f7fa 0%,#eef2f6 45%,#dfe7ef 100%)}
.hero-photo{left:586px;top:0;width:614px;height:571px;background:linear-gradient(180deg,#c9d7e4 0%,#6f8aa6 55%,#2c3f58 100%)}
.hero-fade{left:420px;top:0;width:260px;height:571px;background:linear-gradient(90deg,#f1f4f8,rgba(241,244,248,0))}
.hero h1{left:109px;top:140px;font-size:46px;font-weight:700;color:var(--blue);letter-spacing:-.3px;white-space:nowrap}
.hero .sub{left:111px;top:206px;font-size:18px;color:#2a2e33}
.hero .lead{left:111px;top:242px;width:470px;font-size:14.5px;line-height:24px;color:#40454b}
.hero .btn{left:112px;top:336px;width:182px;height:47px}
.dots{left:572px;top:447px;display:flex;gap:8px}
.dots span{width:8px;height:8px;background:#fff}
.dots span.on{background:var(--blue)}
.hero-edge{left:0;top:0}

/* about */
.about{top:660px;height:614px}
.about-photo{left:87px;top:0;width:484px;height:507px;background:linear-gradient(160deg,#e9eef3 0%,#b9c8d8 55%,#2d4663 100%)}
.about .eyebrow{left:623px;top:77px}
.about .title{left:622px;top:108px;font-size:42px}
.about .rule{left:623px;top:174px}
.about p{left:623px;width:430px;font-size:14.5px;line-height:24px;color:#40454b}
.about .p1{top:197px}
.about .p2{top:318px}
.about .btn{left:623px;top:438px;width:165px;height:47px}

/* services */
.services{top:1274px;height:685px;background:linear-gradient(180deg,#2a84c9 0%,#1f78c0 60%,#1a6fb6 100%)}
.services .eyebrow{color:#fff;top:64px}
.services .title{color:#fff;top:92px;font-size:48px}
.services .rule{background:#fff;left:575px;top:162px}
.services .desc{top:185px;font-size:15px;line-height:24px;color:#fff}
.card{top:267px;width:233px;background:#fff}
.card .img{height:259px}
.card .label{display:flex;align-items:center;justify-content:center;text-align:center;font-size:16.5px;font-weight:700;color:var(--ink);line-height:24px;height:50px}
.card.tall .label{height:72px}

/* why */
.why{top:1959px;height:641px}
.why .eyebrow{top:88px}
.why .title{top:118px;font-size:46px}
.why .rule{left:575px;top:180px}
.ring{left:429px;top:236px;width:342px;height:342px;border-radius:50%;border:14px solid #f4f4f4;box-shadow:0 0 0 1px #ebebeb inset}
.icon{width:80px;height:80px;border-radius:50%;background:#fff;border:2px solid var(--blue);display:flex;align-items:center;justify-content:center}
.icon::before{content:"";position:absolute;inset:5px;border-radius:50%;border:1.5px solid #333}
.why .label{font-size:26px;font-weight:700;color:var(--ink);white-space:nowrap}

/* testimonials */
.testimonials{top:2600px;height:654px;background:var(--grey-bg)}
.testimonials .eyebrow{top:131px}
.testimonials .title{top:157px;font-size:48px}
.testimonials .rule{left:575px;top:219px}
.quote-card{top:258px;width:475px;height:290px;background:#fff}
.quote-card .mark{position:absolute;left:31px;top:20px}
.quote-card p{position:absolute;left:32px;top:100px;width:405px;font-size:17px;line-height:26px;color:#3a3f45}
.quote-card .who{position:absolute;left:32px;top:210px;font-size:20px;font-weight:700;color:var(--ink)}
.quote-card .org{position:absolute;left:32px;top:243px;font-size:15.5px;color:var(--muted)}

/* contact */
.contact{top:3254px;height:442px;background:linear-gradient(110deg,#2a68c6 0%,#2479cc 55%,#2a97da 100%)}
.contact .eyebrow{color:#fff;top:92px}
.contact .title{color:#fff;top:120px;font-size:44px}
.contact .rule{background:#fff;left:575px;top:186px}
.contact .desc{top:217px;font-size:17px;line-height:26px;color:#fff}
.contact .btn-outline{left:472px;top:309px;width:225px;height:48px;display:flex;align-items:center;justify-content:center;color:#fff;font-size:17px;font-weight:500;letter-spacing:.3px}

/* footer */
.site-footer{top:3696px;height:385px;background:var(--footer-bg)}
.footer-brand{top:110px;font-size:44px;font-weight:700;color:var(--ink);line-height:52px}
.footer-slogan{top:211px;font-size:17px;font-weight:500;color:var(--blue)}
.footer-links{top:263px;font-size:17px;color:var(--ink)}
.footer-links span{margin:0 12px;color:var(--blue)}
.copyright{top:318px;font-size:17px;color:var(--ink)}
</style>
</head>
<body>

<header class="section site-header">
  <div class="abs brand">Brightpath Consult</div>
  <nav class="abs nav">
    <a class="active" style="left:0">HOME</a>
    <a style="left:79px">ABOUT</a>
    <a style="left:164px">SERVICES</a>
    <a style="left:270px">WHY CHOOSE BRIGHTPATH</a>
    <a style="left:488px">CONTACT</a>
    <a style="left:600px;color:var(--blue)">EN ▾</a>
  </nav>
</header>

<section class="section hero">
  <div class="abs hero-photo" role="img" aria-label="Two business professionals in an office looking at a tablet and phone"></div>
  <div class="abs hero-fade"></div>
  <h1 class="abs">BRIGHTPATH CONSULT</h1>
  <div class="abs sub">Shaping Leaders. Empowering Teams. Driving Change.</div>
  <p class="abs lead">We partner with global organizations to unlock leadership potential, strengthen specialist expertise, and create inclusive workplaces where people thrive.</p>
  <a class="abs btn">Get Started</a>
  <div class="abs dots"><span class="on"></span><span></span><span></span><span></span></div>
  <svg class="abs hero-edge" width="1200" height="571" viewBox="0 0 1200 571">
    <polygon points="0,562 600,492 1200,568 1200,571 0,571" fill="#fff"/>
    <polygon points="0,545 600,474 1200,552 1200,568 600,492 0,562" fill="#1f7ac4"/>
  </svg>
</section>

<section class="section about">
  <div class="abs about-photo" role="img" aria-label="Portrait of the consultant in a suit"></div>
  <div class="abs eyebrow">ABOUT ME</div>
  <h2 class="abs title">BRIGHTPATH CONSULT</h2>
  <div class="abs rule"></div>
  <p class="abs p1">At Brightpath Consult, we believe leadership is not a title—it's a responsibility. Our consultancy is dedicated to developing leaders and specialists who drive results, inspire teams, and shape future-ready organizations.</p>
  <p class="abs p2">With years of international experience in leadership development, team facilitation, and organizational strategy, we bring a unique blend of knowledge, empathy, and practical tools to help businesses grow from the inside out.</p>
  <a class="abs btn">Read More</a>
</section>

<section class="section services">
  <div class="abs center eyebrow">WHAT WE DO</div>
  <h2 class="abs center title">OUR SERVICES</h2>
  <div class="abs rule"></div>
  <p class="abs center desc">We design and deliver tailored programs that equip leaders and specialists with the tools to<br>succeed in a complex, global business environment.</p>
  <div class="abs card" style="left:111px">
    <div class="img" role="img" aria-label="Presenter leading a corporate academy session" style="background:linear-gradient(160deg,#8a7a66,#3b3530)"></div>
    <div class="label">Corporate Academies</div>
  </div>
  <div class="abs card tall" style="left:359px">
    <div class="img" role="img" aria-label="Team collaborating around a laptop" style="background:linear-gradient(160deg,#4b5866,#2a2f36)"></div>
    <div class="label">Leadership &amp;<br>Team Development</div>
  </div>
  <div class="abs card" style="left:607px">
    <div class="img" role="img" aria-label="Colleagues in a strategy discussion" style="background:linear-gradient(160deg,#b6aca3,#7a4c45)"></div>
    <div class="label">Strategy Facilitation</div>
  </div>
  <div class="abs card" style="left:855px">
    <div class="img" role="img" aria-label="Coaching session in a bright meeting room" style="background:linear-gradient(160deg,#d4cbc2,#6e7d8c)"></div>
    <div class="label">Coaching</div>
  </div>
</section>

<section class="section why">
  <div class="abs center eyebrow">WHY PARTNER WITH US?</div>
  <h2 class="abs center title">WHY CHOOSE BRIGHTPATH</h2>
  <div class="abs rule"></div>
  <div class="abs ring"></div>

  <div class="abs icon" style="left:453px;top:263px">
    <svg width="40" height="40" viewBox="0 0 40 40" fill="none" stroke="#222" stroke-width="1.6"><circle cx="20" cy="20" r="16"/><ellipse cx="20" cy="20" rx="7" ry="16"/><line x1="4" y1="20" x2="36" y2="20"/><line x1="7" y1="12" x2="33" y2="12"/><line x1="7" y1="28" x2="33" y2="28"/></svg>
  </div>
  <div class="abs icon" style="left:668px;top:263px">
    <svg width="40" height="40" viewBox="0 0 40 40" fill="none" stroke="#222" stroke-width="1.8"><circle cx="20" cy="20" r="12"/><polyline points="14,20 18,24 26,15"/></svg>
  </div>
  <div class="abs icon" style="left:458px;top:478px">
    <svg width="40" height="40" viewBox="0 0 40 40" fill="none" stroke="#222" stroke-width="1.6"><circle cx="20" cy="18" r="6"/><circle cx="20" cy="18" r="11" stroke-dasharray="4 3"/><path d="M6 34h10l8-3"/></svg>
  </div>
  <div class="abs icon" style="left:664px;top:481px">
    <svg width="40" height="40" viewBox="0 0 40 40" fill="none" stroke="#222" stroke-width="1.8"><circle cx="20" cy="20" r="13"/><polyline points="20,12 20,20 26,23"/></svg>
  </div>

  <div class="abs label" style="right:772px;top:284px">Global Perspective</div>
  <div class="abs label" style="left:773px;top:284px">Proven Methods</div>
  <div class="abs label" style="right:774px;top:500px">Tailored Approach</div>
  <div class="abs label" style="left:770px;top:503px">Lasting Impact</div>
</section>

<section class="section testimonials">
  <svg class="abs" style="left:0;top:0" width="1200" height="130" viewBox="0 0 1200 130">
    <polygon points="0,0 1200,0 1200,108 600,36 0,100" fill="#fff"/>
    <polygon points="0,100 600,36 1200,108 1200,124 600,52 0,116" fill="#1f7ac4"/>
  </svg>
  <div class="abs center eyebrow">TESTIMONIALS</div>
  <h2 class="abs center title">CLIENT STORIES</h2>
  <div class="abs rule"></div>

  <article class="abs quote-card" style="left:111px">
    <svg class="mark" width="80" height="58" viewBox="0 0 80 58" fill="#1f7ac4"><path d="M20 0a18 18 0 0 1 18 18c0 18-14 32-26 40l-3-4c8-8 10-14 10-18A18 18 0 0 1 20 0z"/><path d="M62 0a18 18 0 0 1 18 18c0 18-14 32-26 40l-3-4c8-8 10-14 10-18A18 18 0 0 1 62 0z"/></svg>
    <p>Brightpath Consult helped us create a leadership academy that transformed the way we develop talent. Their facilitation style is engaging, practical, and deeply impactful.</p>
    <div class="who">HR Director</div>
    <div class="org">Global Manufacturing Company</div>
  </article>
  <article class="abs quote-card" style="left:612px">
    <svg class="mark" width="80" height="58" viewBox="0 0 80 58" fill="#1f7ac4"><path d="M20 0a18 18 0 0 1 18 18c0 18-14 32-26 40l-3-4c8-8 10-14 10-18A18 18 0 0 1 20 0z"/><path d="M62 0a18 18 0 0 1 18 18c0 18-14 32-26 40l-3-4c8-8 10-14 10-18A18 18 0 0 1 62 0z"/></svg>
    <p>Brightpath Consult helped us create a leadership academy that transformed the way we develop talent. Their facilitation style is engaging, practical, and deeply impactful.</p>
    <div class="who">HR Director</div>
    <div class="org">Global Manufacturing Company</div>
  </article>
</section>

<section class="section contact">
  <div class="abs center eyebrow">CONTACT US</div>
  <h2 class="abs center title">READY TO TAKE THE NEXT STEP?</h2>
  <div class="abs rule"></div>
  <p class="abs center desc">Whether you need a tailored leadership program, a strategy workshop, or one-on-one<br>coaching, Brightpath Consult is here to help your organization thrive.</p>
  <a class="abs btn-outline">
    <svg class="abs" style="left:0;top:0" width="225" height="48" viewBox="0 0 225 48"><polygon points="12,1 224,1 213,47 1,47" fill="none" stroke="#fff" stroke-width="2"/></svg>
    <span style="position:relative">CONTACT US TODAY</span>
  </a>
</section>

<footer class="section site-footer">
  <div class="abs center footer-brand">Brightpath Consult</div>
  <div class="abs center footer-slogan">Brightpath Consult – Shaping Leaders. Empowering Teams. Driving Change.</div>
  <div class="abs center footer-links">Home<span>|</span>About<span>|</span>Services<span>|</span>Contact</div>
  <div class="abs center copyright">© 2025 Brightpath Consult. All rights reserved.</div>
</footer>

</body>
</html>
```